Pebble Lane Sweets Sweets - Shopify Website Design

A monthly subscription company. Need a Shopify Website Design and uploaded to fully work with Kestrel Renewals.

Please look at these sites for examples as well as the images I enclosed.

http://pebblelanesweets.example
https://www.lumora-vx.example/
https://www.platewisp.example/
https://www.globalnibblo.example/
https://www.sipmarto.example/
https://grindcrate.example/

```html
<!DOCTYPE html>
<html lang="en">
<head>
<meta charset="utf-8">
<title>Pebble Lane Sweets – Website Design</title>
<link href="https://fonts.googleapis.com/css2?family=Montserrat:wght@400;500;600;700;800&display=swap" rel="stylesheet">
<style>
:root{
  --red:#d81f3b;
  --ink:#222;
  --muted:#777;
  --card:#f4f4f4;
  --orange:#f6a623;
  --orange-deep:#e8871a;
  --sky:#bfe6f0;
  --blue:#3fc1e2;
  --dark:#121212;
  --darker:#0b0b0b;
  --pink:#ef7fb0;
}
*{box-sizing:border-box;margin:0;padding:0}
html,body{width:1200px;height:3494px;overflow:hidden;background:#fff;font-family:"Montserrat",sans-serif;color:var(--ink)}
.board{position:relative;width:1200px;height:3494px}

.brand-title{position:absolute;top:170px;left:0;width:1200px;display:flex;align-items:center;justify-content:center;gap:24px}
.brand-title .dot{width:46px;height:46px;border-radius:50%;background:var(--pink)}
.brand-title h1{font-size:76px;font-weight:800;color:var(--red);letter-spacing:2px}

.screen{position:absolute;left:233px;top:331px;width:733px;height:413px;overflow:hidden;box-shadow:0 0 0 1px #ddd}
.screen .page{transform:scale(1.386);transform-origin:0 0;position:absolute;left:0;top:0}

.page{position:absolute;width:529px;height:2419px;background:#fff;overflow:hidden;font-size:5px}
.page.left{left:49px;top:1024px}
.page.right{left:620px;top:1024px}
.abs{position:absolute}

.topbar{left:0;top:0;width:529px;height:15px;background:var(--dark);color:#fff;display:flex;align-items:center;justify-content:center;font-size:4.5px}
.topbar .socials{position:absolute;right:12px;top:4.5px;display:flex;gap:4px}
.topbar .socials i{width:6px;height:6px;border-radius:50%;background:#fff;display:block}
.nav{left:0;top:15px;width:529px;height:30px;display:flex;align-items:center;padding:0 40px;font-size:4.6px;font-weight:500}
.nav .links,.nav .tools{display:flex;gap:11px}
.nav .logo{position:absolute;left:0;width:529px;text-align:center;top:11px;font-size:8px;font-weight:700;color:var(--red)}
.nav .tools{margin-left:auto}

.hero{left:0;top:45px;width:529px;height:254px;background:
  radial-gradient(circle at 4% 35%,#2a2230 0,#2a2230 9%,transparent 16%),
  radial-gradient(circle at 6% 78%,#2a2230 0,#2a2230 9%,transparent 17%),
  radial-gradient(circle at 92% 14%,#f08a1c 0,#f08a1c 9%,transparent 16%),
  radial-gradient(circle at 88% 82%,#2a2230 0,#2a2230 8%,transparent 15%),
  radial-gradient(circle at 22% 92%,#f08a1c 0,#f08a1c 6%,transparent 12%),
  radial-gradient(circle at 50% 45%,#fbc56a 0%,var(--orange) 50%,var(--orange-deep) 100%)}
.hero-copy{left:0;top:112px;width:529px;text-align:center;font-size:13.5px;font-weight:500;line-height:19px;color:#2b2016}
.btn{display:inline-block;background:var(--red);color:#fff;font-weight:600;text-align:center;white-space:nowrap}
.hero .btn{position:absolute;left:214px;top:172px;width:100px;height:22px;line-height:22px;font-size:5.4px}
.hero .arrow{position:absolute;top:130px;width:14px;height:14px;border-radius:50%;background:#fff;font-size:7px;line-height:14px;text-align:center;color:#444}
.hero .dots{position:absolute;top:243px;left:252px;display:flex;gap:4px}
.hero .dots i{width:4px;height:4px;border-radius:50%;background:rgba(255,255,255,.6);display:block}
.hero .dots i.on{background:#fff}

.section-title{left:0;width:529px;text-align:center;color:var(--red);font-size:8px;font-weight:500}

.products{left:45px;width:441px;display:flex;gap:11px}
.product{width:102px;text-align:center}
.product .thumb{height:111px;background:var(--card);display:flex;align-items:center;justify-content:center}
.product .shot{width:78px;height:40px;border-radius:3px}
.product .shot.tall{width:62px;height:72px}
.product .shot.wide{width:86px;height:28px}
.product .name{margin-top:8px;font-size:4.4px}
.product .price{margin-top:3px;font-size:4.2px}
.product .rating{margin-top:3px;font-size:4.2px}
.product .rating b{font-size:5px;letter-spacing:.3px}
.product .btn{margin-top:6px;width:44px;height:11px;line-height:11px;font-size:4.2px}

.tiles{left:45px;width:441px;display:flex;gap:17px}
.tile{width:212px;text-align:center}
.tile .thumb{height:138px}
.tile h3{margin-top:10px;font-size:6.4px;font-weight:500}
.tile p{margin:4px auto 0;width:170px;font-size:3.8px;line-height:5px;color:var(--muted)}
.tile .btn{margin-top:8px;width:90px;height:11px;line-height:11px;font-size:4.2px}

.ship-band{left:0;top:1026px;width:529px;height:189px;background:
  radial-gradient(ellipse at 76% 62%,#f28c3a 0,#5cc96b 14%,#e94d62 24%,transparent 34%),
  radial-gradient(circle at 66% 12%,#e8324a 0,#f4f4f4 8%,transparent 13%),
  linear-gradient(90deg,var(--sky) 0%,#d8f1f7 55%,#a8dbe9 100%)}
.ship-copy{left:44px;top:1083px;width:230px;font-size:8px;line-height:12px;font-weight:500}
.ship-btn{left:44px;top:1125px;width:90px;height:14px;line-height:14px;font-size:4.6px}

.bag-band{left:0;top:1699px;width:529px;height:200px;background:
  radial-gradient(circle at 10% 68%,#f3d24a 0,#e8418a 9%,transparent 15%),
  radial-gradient(circle at 38% 96%,#f3d24a 0,#8b4fd0 8%,transparent 14%),
  radial-gradient(circle at 90% 62%,#f28a2a 0,#e8324a 8%,transparent 14%),
  radial-gradient(circle at 76% 98%,#f4f4f4 0,#e8418a 7%,transparent 12%),
  radial-gradient(circle at 50% 40%,#7ad7ee 0%,var(--blue) 60%,#27a9cd 100%)}
.bag-copy{left:0;top:1747px;width:529px;text-align:center}
.bag-copy h3{font-size:11px;font-weight:500}
.bag-copy p{margin:6px auto 0;width:300px;font-size:4px;line-height:6px}
.bag-copy .btn{margin-top:12px;width:90px;height:12px;line-height:12px;font-size:4.4px}

.posts{left:45px;top:1982px;width:441px;display:flex;gap:12px}
.post{width:139px}
.post .thumb{height:64px}
.post .date{margin-top:6px;font-size:3.4px;color:var(--muted)}
.post h4{margin-top:4px;font-size:4.6px;font-weight:700}
.post p{margin-top:3px;font-size:3.6px;line-height:5px;color:var(--muted)}

.promo-band{left:0;top:2117px;width:529px;height:52px;background:var(--dark);color:#fff;font-size:5px}
.promo-band .item{position:absolute;top:17px;text-align:center}
.promo-band small{display:block;font-size:3.8px;margin-top:2px;color:#ccc}
.mailing{left:0;top:2169px;width:529px;height:48px}
.mailing h4{position:absolute;left:67px;top:18px;font-size:8px;font-weight:500}
.mailing .field{position:absolute;left:267px;top:17px;width:135px;height:14px;border:1px solid #ccc;font-size:3.8px;line-height:12px;padding-left:5px;color:#888}
.mailing .btn{position:absolute;left:402px;top:17px;width:30px;height:14px;line-height:14px;font-size:4px}

.footer{left:0;top:2217px;width:529px;height:202px;background:var(--darker);color:#ddd}
.footer .col{position:absolute;top:30px;font-size:3.6px;line-height:7.5px}
.footer .col h5{font-size:4.4px;font-weight:600;color:#fff;margin-bottom:5px}
.footer .circles{display:flex;gap:3px;margin-top:2px}
.footer .circles i{width:10px;height:10px;border-radius:50%;border:1px solid #ccc;display:block}
.footer .phone{margin-top:10px;font-size:4.4px;color:#fff;line-height:7px}
.footer .btn{margin-top:8px;width:46px;height:14px;line-height:14px;font-size:4.2px}
.footer .copy{position:absolute;bottom:10px;width:529px;text-align:center;font-size:3.6px}

.overlay{left:0;top:0;width:529px;height:2419px;background:rgba(0,0,0,.42)}
.popup{left:96px;top:85px;width:336px;height:156px;background:#fff;display:flex}
.popup .form{width:175px;padding:18px 0 0 14px;text-align:center}
.popup h3{font-size:9px;font-weight:600;text-align:left}
.popup p{margin-top:5px;font-size:3.8px;line-height:5px;text-align:left;font-weight:600}
.popup .line{margin:18px 0 0 6px;width:150px;border-bottom:1px solid #999;font-size:3.4px;padding-bottom:3px;color:#777}
.popup .btn{margin-top:10px;width:42px;height:12px;line-height:12px;font-size:4.4px}
.popup .circles{display:flex;gap:4px;justify-content:center;margin-top:9px}
.popup .circles i{width:5px;height:5px;border-radius:50%;background:#333;display:block}
.popup .visual{margin:24px 0 24px 0;width:140px;border-radius:4px;background:linear-gradient(160deg,#5a2e1e 0%,#8a4a2c 40%,#c0262e 65%,#e24a4a 100%)}
.popup .close{position:absolute;right:8px;top:6px;font-size:9px;color:#333}

.ph-choc{background:linear-gradient(110deg,#f5efe8 0%,#e9ddd0 35%,#a06a42 62%,#5c3420 100%)}
.ph-bulk{background:linear-gradient(100deg,#e94f4f 0%,#7ccf8a 20%,#f2e34a 40%,#e86a9a 60%,#68b8e8 80%,#f29a3a 100%)}
.ph-corp{background:radial-gradient(ellipse at 50% 50%,#2c1a12 0%,#4a2a1a 40%,#9a5a30 75%,#c07a44 100%)}
.ph-wells{background:linear-gradient(180deg,#5e7a3a 0%,#8aa060 35%,#b28a5a 70%,#7a5232 100%)}
.ph-kids{background:linear-gradient(135deg,#4a2418,#a83a22 50%,#d8682e)}
.ph-sweets{background:linear-gradient(120deg,#f25a8a,#f6d24a 35%,#6acb7a 60%,#5ac0e8 85%)}
.ph-desk{background:linear-gradient(135deg,#ede9e4,#b9aca0 55%,#8a7a6e)}
.sh-mix{background:linear-gradient(120deg,#e2342c 0%,#f2c12e 35%,#2e6fc8 65%,#6a3a22 100%)}
.sh-brown{background:linear-gradient(90deg,#4a2c1c,#7a4a2c 50%,#4a2c1c)}
.sh-cocoa{background:linear-gradient(90deg,#3e2418,#6a4030 50%,#3e2418)}
.sh-cream{background:linear-gradient(90deg,#efe4d2,#c9342c 50%,#efe4d2)}
.sh-red{background:linear-gradient(135deg,#e8392c,#c21f1f)}
.sh-orange{background:linear-gradient(180deg,#e9862a,#4a2c1c 55%,#d92a2a)}
.sh-blue{background:linear-gradient(135deg,#3a8fd8,#f2c12e 55%,#c7302a)}
.sh-yellow{background:linear-gradient(135deg,#f4c431,#e88a2a 60%,#c8342a)}
.sh-navy{background:linear-gradient(135deg,#2e3f8a,#f2c12e 55%,#8a2a1c)}
</style>
</head>
<body>
<div class="board">

  <div class="brand-title"><span class="dot"></span><h1>Pebble Lane Sweets</h1></div>

  <!-- Desktop view: header and hero -->
  <div class="screen">
    <div class="page">
      <div class="abs topbar">Receive 20% off your next order using code 'Candy life'<div class="socials"><i></i><i></i><i></i><i></i></div></div>
      <div class="abs nav">
        <div class="links"><span>Home</span><span>Shop Candy ⌄</span><span>Blog</span><span>FAQs</span><span>Contact</span></div>
        <div class="logo">Pebble Lane Sweets</div>
        <div class="tools"><span>USD $ ⌄</span><span>⌕ Search</span><span>Account</span><span>Cart - 0</span></div>
      </div>
      <div class="abs hero" role="img" aria-label="Halloween banner with pumpkins, balloons, bats and candy on orange">
        <span class="arrow" style="left:14px">‹</span><span class="arrow" style="right:14px">›</span>
        <a class="btn">SHOP SPOOKY SWEETS</a>
        <div class="dots"><i></i><i></i><i class="on"></i><i></i></div>
      </div>
      <div class="abs hero-copy">GET 15% OFF SITE-WIDE THIS<br>HALLOWEEN WITH CODE<br>‘PEBBLESWEB’</div>
    </div>
  </div>

  <!-- Home page: with sign-up pop-up -->
  <div class="page left">
    <div class="abs topbar">Receive 20% off your next order using code 'Candy life'<div class="socials"><i></i><i></i><i></i><i></i></div></div>
    <div class="abs nav">
      <div class="links"><span>Home</span><span>Shop Candy ⌄</span><span>Blog</span><span>FAQs</span><span>Contact</span></div>
      <div class="logo">Pebble Lane Sweets</div>
      <div class="tools"><span>USD $ ⌄</span><span>⌕ Search</span><span>Account</span><span>Cart - 0</span></div>
    </div>
    <div class="abs hero" role="img" aria-label="Halloween banner with pumpkins, balloons, bats and candy on orange">
      <span class="arrow" style="left:14px">‹</span><span class="arrow" style="right:14px">›</span>
      <div class="dots"><i></i><i></i><i class="on"></i><i></i></div>
    </div>

    <div class="abs section-title" style="top:336px">RECOMMENDED FOR YOU</div>
    <div class="abs products" style="top:353px">
      <div class="product"><div class="thumb"><div class="shot tall sh-mix" role="img" aria-label="Pile of assorted candy bars"></div></div><div class="name">Decade Candy Gift Box</div><div class="price">From $27.99</div><div class="rating"><b>★★★★☆</b> 2 reviews</div><a class="btn">Add To Cart</a></div>
      <div class="product"><div class="thumb"><div class="shot wide sh-brown" role="img" aria-label="Chocolate bar in wrapper"></div></div><div class="name">Zippa Taffy - 1.8 Oz Bar</div><div class="price">From $27.99</div><div class="rating"><b>★★★★☆</b> 2 reviews</div><a class="btn">Add To Cart</a></div>
      <div class="product"><div class="thumb"><div class="shot sh-cocoa" role="img" aria-label="Dark chocolate bar in wrapper"></div></div><div class="name">Zippa Taffy - 1.8 Oz Bar</div><div class="price">From $27.99</div><div class="rating"><b>★★★★☆</b> 2 reviews</div><a class="btn">Add To Cart</a></div>
      <div class="product"><div class="thumb"><div class="shot sh-cream" role="img" aria-label="Box of malted milk balls"></div></div><div class="name">Zippa Taffy - 1.8 Oz Bar</div><div class="price">From $27.99</div><div class="rating"><b>★★★★☆</b> 2 reviews</div><a class="btn">Add To Cart</a></div>
    </div>

    <div class="abs tiles" style="top:564px">
      <div class="tile"><div class="thumb ph-choc" role="img" aria-label="Chocolates in a gift box with ribbon"></div><h3>SUBSCRIPTION BOXES</h3><p>Lorem ipsum dolor sit amet, consectetur adipiscing elit, sed do eiusmod tempor incididunt ut labore et dolore magna</p><a class="btn">Shop Subscription Boxes</a></div>
      <div class="tile"><div class="thumb ph-bulk" role="img" aria-label="Trays of colourful bulk candy"></div><h3>RETRO CANDY IN BULK</h3><p>Lorem ipsum dolor sit amet, consectetur adipiscing elit, sed do eiusmod tempor incididunt ut labore et dolore magna</p><a class="btn">Shop Bulk Candy</a></div>
    </div>
    <div class="abs tiles" style="top:779px">
      <div class="tile"><div class="thumb ph-corp" role="img" aria-label="Box of assorted chocolates"></div><h3>CORPORATE GIFTS</h3><p>Lorem ipsum dolor sit amet, consectetur adipiscing elit, sed do eiusmod tempor incididunt ut labore et dolore magna</p><a class="btn">Shop Corp Gifts</a></div>
      <div class="tile"><div class="thumb ph-wells" role="img" aria-label="Children carrying water on a dirt path"></div><h3>WATER WELLS FOR AFRICA</h3><p>Lorem ipsum dolor sit amet, consectetur adipiscing elit, sed do eiusmod tempor incididunt ut labore et dolore magna</p><a class="btn">Donate</a></div>
    </div>

    <div class="abs ship-band" role="img" aria-label="Lollipops and a jar of jelly beans on light blue"></div>
    <div class="abs ship-copy">$9.95 FLAT-RATE SHIPPING FOR US ORDERS LOWER 48 STATES).FREE SHIPPING FOR ALL US ORDERS OVER $250.</div>
    <a class="abs btn ship-btn">Search Candys</a>

    <div class="abs section-title" style="top:1253px">SOME OF OUR FAVORITES</div>
    <div class="abs products" style="top:1272px">
      <div class="product"><div class="thumb"><div class="shot sh-red" role="img" aria-label="Wafer bar in red wrapper"></div></div><div class="name">Decade Candy Gift Box</div><div class="price">From $27.99</div><div class="rating"><b>★★★★☆</b> 2 reviews</div><a class="btn">Add To Cart</a></div>
      <div class="product"><div class="thumb"><div class="shot tall sh-orange" role="img" aria-label="Stack of candy bars"></div></div><div class="name">Decade Candy Gift Box</div><div class="price">From $27.99</div><div class="rating"><b>★★★★☆</b> 2 reviews</div><a class="btn">Add To Cart</a></div>
      <div class="product"><div class="thumb"><div class="shot wide sh-cocoa" role="img" aria-label="Chocolate bar in wrapper"></div></div><div class="name">Decade Candy Gift Box</div><div class="price">From $27.99</div><div class="rating"><b>★★★★☆</b> 2 reviews</div><a class="btn">Add To Cart</a></div>
      <div class="product"><div class="thumb"><div class="shot sh-navy" role="img" aria-label="Assorted candy bars"></div></div><div class="name">Decade Candy Gift Box</div><div class="price">From $27.99</div><div class="rating"><b>★★★★☆</b> 2 reviews</div><a class="btn">Add To Cart</a></div>
    </div>
    <div class="abs products" style="top:1465px">
      <div class="product"><div class="thumb"><div class="shot tall sh-blue" role="img" aria-label="Box of chocolate covered raisins"></div></div><div class="name">Decade Candy Gift Box</div><div class="price">From $27.99</div><div class="rating"><b>★★★★☆</b> 2 reviews</div><a class="btn">Add To Cart</a></div>
      <div class="product"><div class="thumb"><div class="shot tall sh-yellow" role="img" aria-label="Bag of gummy bears"></div></div><div class="name">Decade Candy Gift Box</div><div class="price">From $27.99</div><div class="rating"><b>★★★★☆</b> 2 reviews</div><a class="btn">Add To Cart</a></div>
      <div class="product"><div class="thumb"><div class="shot tall sh-orange" role="img" aria-label="Stack of candy bars"></div></div><div class="name">Decade Candy Gift Box</div><div class="price">From $27.99</div><div class="rating"><b>★★★★☆</b> 2 reviews</div><a class="btn">Add To Cart</a></div>
      <div class="product"><div class="thumb"><div class="shot sh-navy" role="img" aria-label="Candy bars in blue wrappers"></div></div><div class="name">Decade Candy Gift Box</div><div class="price">From $27.99</div><div class="rating"><b>★★★★☆</b> 2 reviews</div><a class="btn">Add To Cart</a></div>
    </div>

    <div class="abs bag-band" role="img" aria-label="Swirl lollipops and scattered candy on blue"></div>
    <div class="abs bag-copy"><h3>PACK-A-BAG</h3><p>Lorem ipsum dolor sit amet, consectetur adipiscing elit, sed do eiusmod tempor incididunt ut labore et dolore magna aliqua. Quis ipsum suspendisse ultrices gravida. Lorem ipsum dolor sit amet, consectetur adipiscing elit, sed do eiusmod tempor</p><a class="btn">Start Your Bag</a></div>

    <div class="abs section-title" style="top:1929px">WHAT'S NEW?</div>
    <div class="abs posts">
      <div class="post"><div class="thumb ph-kids" role="img" aria-label="Children in costumes with a candy bucket"></div><div class="date">September 20, 2020</div><h4>Lorem ipsum dolor sit amet, ur adipiscing</h4><p>Lorem ipsum dolor sit amet, consectetur adipiscing elit, sed do eiusmod tempor incididunt ut labore</p></div>
      <div class="post"><div class="thumb ph-sweets" role="img" aria-label="Pile of colourful sweets"></div><div class="date">September 20, 2020</div><h4>Lorem ipsum dolor sit amet, ur adipiscing</h4><p>Lorem ipsum dolor sit amet, consectetur adipiscing elit, sed do eiusmod tempor incididunt ut labore</p></div>
      <div class="post"><div class="thumb ph-desk" role="img" aria-label="Child at a desk with a laptop"></div><div class="date">September 20, 2020</div><h4>Lorem ipsum dolor sit amet, ur adipiscing</h4><p>Lorem ipsum dolor sit amet, consectetur adipiscing elit, sed do eiusmod tempor incididunt ut labore</p></div>
    </div>

    <div class="abs promo-band">
      <div class="item" style="left:60px">Free Delivery Worldwide<small>Click here for more info</small></div>
      <div class="item" style="right:68px">Final Clearance Sale<small>Up to 70% off</small></div>
    </div>
    <div class="abs mailing"><h4>JOIN OUR MAILING LIST</h4><div class="field">Enter email</div><a class="btn">Subscribe</a></div>

    <div class="abs footer">
      <div class="col" style="left:44px"><h5>CUSTOMER SERVICE</h5>FAQs<br>Shipping<br>$9.95 Flat-rate Shipping<br>Apo/fpo Shipping<br>Candy Coins (Rewards)<br>Terms &amp; Conditions<br>Corporate Gifts<br>Phone Orders<br>Coupon Codes</div>
      <div class="col" style="left:139px"><h5>SAFE SHOPPING</h5>100% Satisfaction<br>Security<br>Privacy Policy<br>Fair Trade Register<br>Shipping Insurance</div>
      <div class="col" style="left:228px"><h5>ABOUT US</h5>History &amp; Mission<br>Water Wells For Africa<br>Candy Blog<br>Reward For Finding Site<br>Errors</div>
      <div class="col" style="left:327px"><h5>QUICK LINKS</h5>Bulk Candy<br>Candy By Brands<br>Candy By Color<br>Retro Toys<br>Party Favors<br>Gift Card<br>Candy On Sale<br>Discontinued Candy<br>Affiliate Programs<br>Candy Museum</div>
      <div class="col" style="left:415px"><h5>FOLLOW US</h5><div class="circles"><i></i><i></i><i></i><i></i></div><div class="phone">☏ 1-888-888-8888<br>9AM - 4PM EST<br>MON - FRI</div><a class="btn">CONTACT US</a></div>
      <div class="copy">© 2020 PEBBLE LANE SWEETS , ALL RIGHTS RESERVED</div>
    </div>

    <div class="abs overlay"></div>
    <div class="abs popup">
      <div class="form">
        <h3>Get your candys every week!</h3>
        <p>Lorem ipsum dolor sit amet, consectetur adipiscing elit, sed do eiusmod tempor incididunt ut labore</p>
        <div class="line">Enter your email address</div>
        <a class="btn">Subscribe</a>
        <div class="circles"><i></i><i></i><i></i><i></i></div>
      </div>
      <div class="visual" role="img" aria-label="Open red box of assorted chocolates"></div>
      <span class="close">×</span>
    </div>
  </div>

  <!-- Home page -->
  <div class="page right">
    <div class="abs topbar">Receive 20% off your next order using code 'Candy life'<div class="socials"><i></i><i></i><i></i><i></i></div></div>
    <div class="abs nav">
      <div class="links"><span>Home</span><span>Shop Candy ⌄</span><span>Blog</span><span>FAQs</span><span>Contact</span></div>
      <div class="logo">Pebble Lane Sweets</div>
      <div class="tools"><span>USD $ ⌄</span><span>⌕ Search</span><span>Account</span><span>Cart - 0</span></div>
    </div>
    <div class="abs hero" role="img" aria-label="Halloween banner with pumpkins, balloons, bats and candy on orange">
      <span class="arrow" style="left:14px">‹</span><span class="arrow" style="right:14px">›</span>
      <a class="btn">SHOP SPOOKY SWEETS</a>
      <div class="dots"><i></i><i></i><i class="on"></i><i></i></div>
    </div>
    <div class="abs hero-copy">GET 15% OFF SITE-WIDE THIS<br>HALLOWEEN WITH CODE<br>‘PEBBLESWEB’</div>

    <div class="abs section-title" style="top:336px">RECOMMENDED FOR YOU</div>
    <div class="abs products" style="top:353px">
      <div class="product"><div class="thumb"><div class="shot tall sh-mix" role="img" aria-label="Pile of assorted candy bars"></div></div><div class="name">Decade Candy Gift Box</div><div class="price">From $27.99</div><div class="rating"><b>★★★★☆</b> 2 reviews</div><a class="btn">Add To Cart</a></div>
      <div class="product"><div class="thumb"><div class="shot wide sh-brown" role="img" aria-label="Chocolate bar in wrapper"></div></div><div class="name">Zippa Taffy - 1.8 Oz Bar</div><div class="price">From $27.99</div><div class="rating"><b>★★★★☆</b> 2 reviews</div><a class="btn">Add To Cart</a></div>
      <div class="product"><div class="thumb"><div class="shot sh-cocoa" role="img" aria-label="Dark chocolate bar in wrapper"></div></div><div class="name">Zippa Taffy - 1.8 Oz Bar</div><div class="price">From $27.99</div><div class="rating"><b>★★★★☆</b> 2 reviews</div><a class="btn">Add To Cart</a></div>
      <div class="product"><div class="thumb"><div class="shot sh-cream" role="img" aria-label="Box of malted milk balls"></div></div><div class="name">Zippa Taffy - 1.8 Oz Bar</div><div class="price">From $27.99</div><div class="rating"><b>★★★★☆</b> 2 reviews</div><a class="btn">Add To Cart</a></div>
    </div>

    <div class="abs tiles" style="top:564px">
      <div class="tile"><div class="thumb ph-choc" role="img" aria-label="Chocolates in a gift box with ribbon"></div><h3>SUBSCRIPTION BOXES</h3><p>Lorem ipsum dolor sit amet, consectetur adipiscing elit, sed do eiusmod tempor incididunt ut labore et dolore magna</p><a class="btn">Shop Subscription Boxes</a></div>
      <div class="tile"><div class="thumb ph-bulk" role="img" aria-label="Trays of colourful bulk candy"></div><h3>RETRO CANDY IN BULK</h3><p>Lorem ipsum dolor sit amet, consectetur adipiscing elit, sed do eiusmod tempor incididunt ut labore et dolore magna</p><a class="btn">Shop Bulk Candy</a></div>
    </div>
    <div class="abs tiles" style="top:779px">
      <div class="tile"><div class="thumb ph-corp" role="img" aria-label="Box of assorted chocolates"></div><h3>CORPORATE GIFTS</h3><p>Lorem ipsum dolor sit amet, consectetur adipiscing elit, sed do eiusmod tempor incididunt ut labore et dolore magna</p><a class="btn">Shop Corp Gifts</a></div>
      <div class="tile"><div class="thumb ph-wells" role="img" aria-label="Children carrying water on a dirt path"></div><h3>WATER WELLS FOR AFRICA</h3><p>Lorem ipsum dolor sit amet, consectetur adipiscing elit, sed do eiusmod tempor incididunt ut labore et dolore magna</p><a class="btn">Donate</a></div>
    </div>

    <div class="abs ship-band" role="img" aria-label="Lollipops and a jar of jelly beans on light blue"></div>
    <div class="abs ship-copy">$9.95 FLAT-RATE SHIPPING FOR US ORDERS LOWER 48 STATES).FREE SHIPPING FOR ALL US ORDERS OVER $250.</div>
    <a class="abs btn ship-btn">Search Candys</a>

    <div class="abs section-title" style="top:1253px">SOME OF OUR FAVORITES</div>
    <div class="abs products" style="top:1272px">
      <div class="product"><div class="thumb"><div class="shot sh-red" role="img" aria-label="Wafer bar in red wrapper"></div></div><div class="name">Decade Candy Gift Box</div><div class="price">From $27.99</div><div class="rating"><b>★★★★☆</b> 2 reviews</div><a class="btn">Add To Cart</a></div>
      <div class="product"><div class="thumb"><div class="shot tall sh-orange" role="img" aria-label="Stack of candy bars"></div></div><div class="name">Decade Candy Gift Box</div><div class="price">From $27.99</div><div class="rating"><b>★★★★☆</b> 2 reviews</div><a class="btn">Add To Cart</a></div>
      <div class="product"><div class="thumb"><div class="shot wide sh-cocoa" role="img" aria-label="Chocolate bar in wrapper"></div></div><div class="name">Decade Candy Gift Box</div><div class="price">From $27.99</div><div class="rating"><b>★★★★☆</b> 2 reviews</div><a class="btn">Add To Cart</a></div>
      <div class="product"><div class="thumb"><div class="shot sh-navy" role="img" aria-label="Assorted candy bars"></div></div><div class="name">Decade Candy Gift Box</div><div class="price">From $27.99</div><div class="rating"><b>★★★★☆</b> 2 reviews</div><a class="btn">Add To Cart</a></div>
    </div>
    <div class="abs products" style="top:1465px">
      <div class="product"><div class="thumb"><div class="shot tall sh-blue" role="img" aria-label="Box of chocolate covered raisins"></div></div><div class="name">Decade Candy Gift Box</div><div class="price">From $27.99</div><div class="rating"><b>★★★★☆</b> 2 reviews</div><a class="btn">Add To Cart</a></div>
      <div class="product"><div class="thumb"><div class="shot tall sh-yellow" role="img" aria-label="Bag of gummy bears"></div></div><div class="name">Decade Candy Gift Box</div><div class="price">From $27.99</div><div class="rating"><b>★★★★☆</b> 2 reviews</div><a class="btn">Add To Cart</a></div>
      <div class="product"><div class="thumb"><div class="shot tall sh-orange" role="img" aria-label="Stack of candy bars"></div></div><div class="name">Decade Candy Gift Box</div><div class="price">From $27.99</div><div class="rating"><b>★★★★☆</b> 2 reviews</div><a class="btn">Add To Cart</a></div>
      <div class="product"><div class="thumb"><div class="shot sh-navy" role="img" aria-label="Candy bars in blue wrappers"></div></div><div class="name">Decade Candy Gift Box</div><div class="price">From $27.99</div><div class="rating"><b>★★★★☆</b> 2 reviews</div><a class="btn">Add To Cart</a></div>
    </div>

    <div class="abs bag-band" role="img" aria-label="Swirl lollipops and scattered candy on blue"></div>
    <div class="abs bag-copy"><h3>PACK-A-BAG</h3><p>Lorem ipsum dolor sit amet, consectetur adipiscing elit, sed do eiusmod tempor incididunt ut labore et dolore magna aliqua. Quis ipsum suspendisse ultrices gravida. Lorem ipsum dolor sit amet, consectetur adipiscing elit, sed do eiusmod tempor</p><a class="btn">Start Your Bag</a></div>

    <div class="abs section-title" style="top:1929px">WHAT'S NEW?</div>
    <div class="abs posts">
      <div class="post"><div class="thumb ph-kids" role="img" aria-label="Children in costumes with a candy bucket"></div><div class="date">September 20, 2020</div><h4>Lorem ipsum dolor sit amet, ur adipiscing</h4><p>Lorem ipsum dolor sit amet, consectetur adipiscing elit, sed do eiusmod tempor incididunt ut labore</p></div>
      <div class="post"><div class="thumb ph-sweets" role="img" aria-label="Pile of colourful sweets"></div><div class="date">September 20, 2020</div><h4>Lorem ipsum dolor sit amet, ur adipiscing</h4><p>Lorem ipsum dolor sit amet, consectetur adipiscing elit, sed do eiusmod tempor incididunt ut labore</p></div>
      <div class="post"><div class="thumb ph-desk" role="img" aria-label="Child at a desk with a laptop"></div><div class="date">September 20, 2020</div><h4>Lorem ipsum dolor sit amet, ur adipiscing</h4><p>Lorem ipsum dolor sit amet, consectetur adipiscing elit, sed do eiusmod tempor incididunt ut labore</p></div>
    </div>

    <div class="abs promo-band">
      <div class="item" style="left:60px">Free Delivery Worldwide<small>Click here for more info</small></div>
      <div class="item" style="right:68px">Final Clearance Sale<small>Up to 70% off</small></div>
    </div>
    <div class="abs mailing"><h4>JOIN OUR MAILING LIST</h4><div class="field">Enter email</div><a class="btn">Subscribe</a></div>

    <div class="abs footer">
      <div class="col" style="left:44px"><h5>CUSTOMER SERVICE</h5>FAQs<br>Shipping<br>$9.95 Flat-rate Shipping<br>Apo/fpo Shipping<br>Candy Coins (Rewards)<br>Terms &amp; Conditions<br>Corporate Gifts<br>Phone Orders<br>Coupon Codes</div>
      <div class="col" style="left:139px"><h5>SAFE SHOPPING</h5>100% Satisfaction<br>Security<br>Privacy Policy<br>Fair Trade Register<br>Shipping Insurance</div>
      <div class="col" style="left:228px"><h5>ABOUT US</h5>History &amp; Mission<br>Water Wells For Africa<br>Candy Blog<br>Reward For Finding Site<br>Errors</div>
      <div class="col" style="left:327px"><h5>QUICK LINKS</h5>Bulk Candy<br>Candy By Brands<br>Candy By Color<br>Retro Toys<br>Party Favors<br>Gift Card<br>Candy On Sale<br>Discontinued Candy<br>Affiliate Programs<br>Candy Museum</div>
      <div class="col" style="left:415px"><h5>FOLLOW US</h5><div class="circles"><i></i><i></i><i></i><i></i></div><div class="phone">☏ 1-888-888-8888<br>9AM - 4PM EST<br>MON - FRI</div><a class="btn">CONTACT US</a></div>
      <div class="copy">© 2020 PEBBLE LANE SWEETS , ALL RIGHTS RESERVED</div>
    </div>
  </div>

</div>
</body>
</html>
```